Spiritual Healer needs design for Wordpress

I am a spiritual healer and I need a Wordpress design to offer my distant healing services on a website. It's like Reiki but I use my own healing modality.
It would be great to have a magical design with beautiful colors like purple, I will upload some images so you get an idea of the feel.
The design should communicate lightness and peacefulness, I like playfulness in the design not too blocky.
Need a complete website design, including navigation bar. I do not have a logo yet.

Target Market(s)

Everyone

Requirements
Nice to have
• Works on mobile devices
Should not have
• Too much of typical spiritual symbols on it.

```html
<!DOCTYPE html>
<html lang="en">
<head>
<meta charset="utf-8">
<title>Moonveil Healing</title>
<link href="https://fonts.googleapis.com/css2?family=Open+Sans:ital,wght@0,400;0,700;1,700&family=Ubuntu:wght@300;400;700&family=Arimo:wght@400&display=swap" rel="stylesheet">
<style>
:root{
  --purple:#6e0a8a;
  --paper:#e9e5dc;
  --ink:#3c3c3c;
  --white:#fff;
  --footer:#2b2928;
  --footer-text:#e6e6e6;
  --link:#1d3f9a;
}
*{box-sizing:border-box;margin:0;padding:0}
html,body{width:1106px;height:1200px;overflow:hidden}
body{background:var(--paper);font-family:"Open Sans",Arial,sans-serif;color:var(--ink);position:relative}
.topline{position:absolute;left:0;top:0;width:1106px;height:5px;background:var(--purple)}
.abs{position:absolute}

.brand{left:98px;top:22px;display:flex;align-items:center;gap:8px}
.brand-dot{width:26px;height:26px;border-radius:50%;background:var(--purple)}
.brand-name{font-family:"Ubuntu",sans-serif;font-weight:700;font-size:30px;color:var(--purple);letter-spacing:-.3px}

.social-top{right:96px;top:13px;display:flex;gap:4px}
.social-sq{width:21px;height:21px;border-radius:3px;background:#7d7d7d;display:block}
.social-sq.c1{background:#3b5a9a}.social-sq.c2{background:#5bb5e6}.social-sq.c3{background:#1b6fa6}
.social-sq.c4{background:#e2762a}.social-sq.c5{background:#6f8fb3}.social-sq.c6{background:#333}

.nav{left:556px;top:48px;display:flex;align-items:center;font-family:"Open Sans",sans-serif;font-weight:700;font-size:11.5px;color:#3a3a3a}
.nav a{color:inherit;text-decoration:none;display:block;line-height:27px}
.nav .active{background:var(--purple);color:var(--white);padding:0 11px}
.nav .i2{margin-left:28px}.nav .i3{margin-left:53px}.nav .i4{margin-left:49px}.nav .i5{margin-left:46px}

.hero{left:95px;top:87px;width:917px;height:391px;background:var(--white);box-shadow:0 14px 18px -10px rgba(0,0,0,.35)}
.hero-art{position:absolute;left:7px;top:8px;width:903px;height:375px;
  background:linear-gradient(135deg,#3a1a66 0%,#5b2d8e 45%,#2a1250 75%,#140a26 100%)}

.card{top:536px;height:148px;background:linear-gradient(#fbfbfb,#ececec);border:2px solid var(--white);border-radius:10px;box-shadow:0 2px 4px rgba(0,0,0,.15)}
.card h2{position:absolute;left:12px;top:7px;display:flex;align-items:center;gap:8px;font-family:"Arimo",Arial,sans-serif;font-weight:400;font-size:19px;color:#444}
.card h2 .mark{width:24px;height:24px;border-radius:50%;background:#9a5ab2}
.card p{position:absolute;left:13px;right:12px;top:43px;font-size:10.3px;line-height:16.5px;text-align:justify;color:#3c3c3c}
.card p em{font-weight:700}
.card .more{position:absolute;right:14px;bottom:8px;font-size:12.5px;color:var(--purple);text-decoration:none}
.c-a{left:92px;width:289px}.c-b{left:415px;width:288px}.c-c{left:724px;width:288px}

.welcome{left:102px;top:724px;font-family:"Ubuntu",sans-serif;font-size:22px;font-weight:300;color:#444}
.welcome strong{font-weight:700;color:var(--purple);font-size:26px}
.photo{left:105px;top:776px;width:169px;height:122px;background:var(--white);padding:5px;box-shadow:0 1px 3px rgba(0,0,0,.3)}
.photo div{width:100%;height:100%;background:linear-gradient(120deg,#1a1040,#7a2a8a 60%,#c05aa0)}
.intro{left:295px;top:774px;width:410px;font-size:10.3px;line-height:16.6px;color:#444;text-align:justify}
.intro b{color:#333}
.intro p+p{margin-top:10px}

.video{left:735px;top:734px;width:261px;height:185px;background:#2e2e2e;border-radius:4px;box-shadow:0 1px 3px rgba(0,0,0,.5)}
.video-art{position:absolute;left:10px;top:8px;width:241px;height:150px;
  background:linear-gradient(135deg,#2a1a6a,#6a2aa0 45%,#a03a6a 70%,#1a0a2a)}
.controls{position:absolute;left:10px;top:160px;width:241px;height:15px;background:linear-gradient(#4a4a4a,#1e1e1e)}

.testimonials{left:94px;top:934px;width:612px;height:165px;background:linear-gradient(var(--white),#f0efec)}
.testimonials h3,.contact h3{font-family:"Arimo",Arial,sans-serif;font-weight:400;font-size:19px;color:#444;position:absolute;left:9px;top:9px}
.avatar{position:absolute;left:19px;top:43px;width:112px;height:112px;border-radius:50%;background:radial-gradient(circle,#fbe6ee 0,#f1c7d6 55%,#d9dde8 100%);border:2px solid #dfe4ea}
.quote{position:absolute;left:149px;top:57px;width:446px;font-size:9.6px;line-height:16.6px;color:#444;text-align:justify}
.qmark{position:absolute;font-family:Georgia,serif;font-size:26px;color:#555;line-height:1}
.arrows{position:absolute;right:12px;top:26px}

.contact{left:735px;top:954px;width:276px;height:146px;background:var(--white)}
.contact address{position:absolute;left:15px;top:40px;font-style:normal;font-family:Arial,sans-serif;font-size:11px;line-height:16px;color:#111}
.contact address .tel{margin-top:4px}
.contact address a{color:var(--link);text-decoration:none;display:block;line-height:15px}

.footer{left:0;top:1121px;width:1106px;height:79px;background:var(--footer);color:var(--footer-text);font-family:Arial,sans-serif}
.footer .follow{position:absolute;left:119px;top:6px;font-size:12.5px}
.footer .social{position:absolute;left:116px;top:24px;display:flex;gap:4px}
.footer .copy{position:absolute;left:115px;top:60px;font-size:10.3px;letter-spacing:.3px}
.footer .links{position:absolute;right:103px;top:7px;font-size:10.3px;letter-spacing:.3px}
.footer .links span{margin:0 5px;color:#bbb}
.footer .meta{position:absolute;right:107px;top:26px;text-align:right;font-size:10.3px;line-height:17px;letter-spacing:.3px}
</style>
</head>
<body>
<div class="topline"></div>

<header>
  <div class="abs brand"><span class="brand-dot"></span><span class="brand-name">Moonveil Healing</span></div>
  <div class="abs social-top" aria-label="Social links">
    <span class="social-sq c1"></span><span class="social-sq c2"></span><span class="social-sq c3"></span>
    <span class="social-sq c4"></span><span class="social-sq c5"></span><span class="social-sq c6"></span>
  </div>
  <nav class="abs nav">
    <a class="active" href="#">HOME</a>
    <a class="i2" href="#">HEALING</a>
    <a class="i3" href="#">EVENTS</a>
    <a class="i4" href="#">WILLOW GLADE</a>
    <a class="i5" href="#">CONTACT</a>
  </nav>
</header>

<section class="abs hero">
  <div class="hero-art" role="img" aria-label="Dreamlike purple night scene with glowing paper lanterns and a zodiac wheel beside a temple facade"></div>
</section>

<section class="abs card c-a">
  <h2><span class="mark"></span>Distant Healing</h2>
  <p><em>If you are unable to attend the Sanctuary for contact healing appointments</em> you may like to try Distant Healing. Requests for yourself, an animal or another for distant healing may be made by letter or email which is read by our healing team.</p>
  <a class="more" href="#">More...</a>
</section>
<section class="abs card c-b">
  <h2><span class="mark"></span>Success Stories</h2>
  <p><em>If you are unable to attend the Sanctuary for contact healing appointments</em> you may like to try Distant Healing. Requests for yourself, an animal or another for distant healing may be made by letter or email which is read by our healing team.</p>
  <a class="more" href="#">More...</a>
</section>
<section class="abs card c-c">
  <h2><span class="mark"></span>Help Us Help You</h2>
  <p><em>If you are unable to attend the Sanctuary for contact healing appointments</em> you may like to try Distant Healing. Requests for yourself, an animal or another for distant healing may be made by letter or email which is read by our healing team.</p>
  <a class="more" href="#">More...</a>
</section>

<h1 class="abs welcome">Welcome to <strong>Moonveil Healing</strong></h1>
<div class="abs photo"><div role="img" aria-label="Glowing hand radiating soft pink healing light on a dark background"></div></div>
<div class="abs intro">
  <p><b>Lorem ipsum dolor sit amet, consectetuer adipiscing elit. Nam nibh. Nunc varius facilisis eros. Sed erat. In in velit quis arcu ornare laoreet.</b> Curabitur adipiscing luctus massa. Integer ut purus ac augue commodo commodo. Nunc nec mi eu justo tempor consectetuer. Etiam vitae nisl. In dignissim lacus ut ante.</p>
  <p>Cras elit lectus, bibendum a, adipiscing vitae, commodo et, dui. Ut tincidunt tortor. Donec nonummy, enim in lacinia pulvinar, velit tellus scelerisque augue, ac posuere libero urna eget neque.....</p>
</div>

<div class="abs video">
  <div class="video-art" role="img" aria-label="Video still of a meditating figure surrounded by rainbow energy swirls"></div>
  <svg class="abs" style="left:108px;top:63px" width="46" height="46" viewBox="0 0 46 46">
    <circle cx="23" cy="23" r="21" fill="rgba(120,120,120,.55)" stroke="#ddd" stroke-width="2"/>
    <path d="M18 13 L33 23 L18 33 Z" fill="#eee"/>
  </svg>
  <div class="controls">
    <svg width="241" height="15" viewBox="0 0 241 15">
      <rect x="5" y="4" width="7" height="7" fill="#bbb"/>
      <rect x="19" y="4" width="2" height="7" fill="#bbb"/><rect x="23" y="4" width="2" height="7" fill="#bbb"/>
      <rect x="44" y="7" width="72" height="1.5" fill="#888"/><rect x="70" y="4" width="5" height="7" fill="#ccc"/>
      <text x="118" y="11" font-family="Arial" font-size="8" fill="#bbb">00:38/01:29</text>
      <path d="M172 6h3l3-3v9l-3-3h-3z" fill="#bbb"/>
      <rect x="190" y="5" width="7" height="6" fill="#999"/><rect x="204" y="5" width="8" height="6" fill="#999"/><rect x="219" y="5" width="8" height="6" fill="#999"/>
    </svg>
  </div>
</div>

<section class="abs testimonials">
  <h3>What others have to say</h3>
  <svg class="arrows" width="28" height="12" viewBox="0 0 28 12"><path d="M8 1 L3 6 L8 11" fill="none" stroke="#666" stroke-width="2.5"/><path d="M20 1 L25 6 L20 11" fill="none" stroke="#666" stroke-width="2.5"/></svg>
  <div class="avatar" role="img" aria-label="Silhouette of a seated meditator before a soft pink lotus"></div>
  <span class="qmark" style="left:131px;top:50px">&ldquo;</span>
  <p class="quote">Lorem ipsum dor to go completely the most amazing product hat allowed us to put ina financing arm to our business, which was not only a convenience to our clients as we becam a one stop shot, but at the same time, through the magic of compound interest we were able to increase our bottom line and make more profit in the space of 12 months of premium funding ourselves than we have made over 20 years of outsourcing&rdquo;.</p>
  <span class="qmark" style="left:544px;top:140px">&rdquo;</span>
</section>

<section class="abs contact">
  <h3>Contact Info</h3>
  <address>
    PO Box 48 27 Lantern Lane<br>
    Willowmere spiritual healer&nbsp; Tasmania<br>
    Australia 7301
    <div class="tel">Telephone 1300 555 014, 1300 555 027</div>
    <a href="#">support@moonveilhealing.com.au</a>
    <a href="#">www.moonveilhealing.com.au</a>
  </address>
</section>

<footer class="abs footer">
  <div class="follow">Follow Us on:</div>
  <div class="social">
    <span class="social-sq c1"></span><span class="social-sq c2"></span><span class="social-sq c3"></span>
    <span class="social-sq c4"></span><span class="social-sq c5"></span><span class="social-sq c6"></span>
  </div>
  <div class="copy">Copyright &copy; 2011 moonveilhealing.com All Rights Reserved.</div>
  <div class="links">Home<span>|</span>About us<span>|</span>Insurance brokers<span>|</span>Accountants<span>|</span>Other professional services<span>|</span>Contact us</div>
  <div class="meta">Brightfund,<br>T:&nbsp; 610.555.0148&nbsp;&nbsp; , F: 610.555.0148<br>E: info@moonveilhealing.com</div>
</footer>
</body>
</html>
```